Service Menu refresh 2018 Update of menu pricing

We currently have service menus as attached. We will be updating our look via our homepage image, our service menu and our in-house beverage and treatment menu.
We are a natural and sustainable hair salon group and moving more towards head spa which consists of treatments, beauty, tanning as well as your traditional hair services. Our imagery needs to reflect our efforts in spa treatments in the hair and scalp area and use natural materials and colours reflecting sustainability.
Elvu is the brand we stock and promote.

Target Market(s)

Men or women interesting in personal maintenance with natural and organic products and using sustainable practises

Industry/Entity Type

Hair And Beauty

Font styles to use
Sans Serif
Other font styles liked:
• Arial or Helvetica

Colors
9acb3c
abd037
cadf82
ffffff

Requirements
Must have
• Name on the front cover, locations on back cover
Nice to have
• Prestige feel, reflect male and female clients
Should not have
• Bold artificial writing or any type of cartoon images.
• Same images as existing menu.

```html
<!DOCTYPE html>
<html lang="en">
<head>
<meta charset="utf-8">
<title>Mossgrove hair salons – Service Menu</title>
<link href="https://fonts.googleapis.com/css2?family=Lato:wght@400;700&display=swap" rel="stylesheet">
<style>
:root{
  --bg:#000;
  --green-light:#1f8445;
  --green-mid:#146a35;
  --green-dark:#0b4221;
  --lime:#9acb3c;
  --lime-soft:#abd037;
  --pale:#cadf82;
  --pill-pale:#c3de95;
  --white:#ffffff;
  --ink-green:#1a6b33;
  --tab:#0a0f0b;
}
*{margin:0;padding:0;box-sizing:border-box}
html,body{width:1098px;height:1200px;overflow:hidden;background:var(--bg);font-family:'Lato',Arial,sans-serif;color:var(--white)}
.card{position:absolute;left:64px;width:970px;height:529px;overflow:hidden;
  background:radial-gradient(ellipse at 55% 40%,var(--green-light) 0%,var(--green-mid) 50%,var(--green-dark) 100%)}
.card--front{top:58px}
.card--back{top:614px}

/* front */
.brand-tab{position:absolute;left:0;top:0;width:412px;height:100px;background:var(--tab);border-bottom-right-radius:70px;display:flex;align-items:center;padding-left:46px;gap:12px}
.brand-dot{width:40px;height:40px;border-radius:50%;background:var(--lime)}
.brand-name{font-size:27px;font-weight:400;color:var(--white);letter-spacing:.2px}
.tagline{position:absolute;left:440px;width:490px;top:32px;text-align:center;font-weight:700;font-size:22.5px;line-height:29px}
.locations{position:absolute;left:40px;top:108px}
.location{position:relative;padding-left:12px;height:80px;font-size:13px;line-height:16px}
.location::before{content:"";position:absolute;left:0;top:3px;width:2px;height:58px;background:var(--lime);border-radius:2px}
.location h3{font-size:13px;font-weight:700;color:var(--lime);text-transform:uppercase}
.photo{position:absolute;left:0;top:0}

/* back */
.pill{position:absolute;top:33px;width:47px;border-radius:24px}
.pill--dark{background:var(--green-mid);border:1px solid var(--pale)}
.pill--pale{background:var(--pill-pale)}
.pill-left{height:395px}
.pill-right{height:339px}
.row{position:absolute;left:0;width:100%;height:16px;line-height:16px;font-size:12px}
.label{position:absolute;white-space:nowrap}
.label--left{left:41px}
.label--right{left:498px}
.sub{font-weight:700;color:var(--lime);font-size:13.5px}
.item{font-size:12px}
.item--caps{text-transform:uppercase;font-size:12px}
.heading{font-size:21.5px;line-height:22px;top:-3px}
.size{font-size:21px;line-height:22px}
.price{position:absolute;width:47px;text-align:center}
.on-dark{color:var(--pale)}
.on-pale{color:var(--ink-green)}
.c-ls{left:253px}.c-lm{left:300px}.c-ll{left:347px}.c-lx{left:393px}
.c-rs{left:726px}.c-rm{left:773px}.c-rl{left:819px}.c-rx{left:866px}
.note{font-size:11.5px}
.notice{position:absolute;left:0;top:452px;width:970px;height:54px;background:var(--white);color:var(--ink-green);font-weight:700;font-size:12.4px;line-height:16px;text-align:center;padding-top:11px}
</style>
</head>
<body>

<section class="card card--front">
  <svg class="photo" width="970" height="529" viewBox="0 0 970 529">
    <defs>
      <linearGradient id="photoTone" x1="0" y1="0" x2="1" y2="1">
        <stop offset="0" stop-color="#f4efea"/>
        <stop offset="0.55" stop-color="#e2c3b0"/>
        <stop offset="1" stop-color="#6b3d2a"/>
      </linearGradient>
    </defs>
    <path d="M460 529 A 560 560 0 0 1 970 112 L970 529 Z" fill="url(#photoTone)" stroke="#0b4221" stroke-width="6" role="img" aria-label="Photo of a woman lying back with eyes closed while receiving a relaxing scalp massage"/>
  </svg>
  <div class="brand-tab">
    <span class="brand-dot"></span>
    <span class="brand-name">Mossgrove hair salons</span>
  </div>
  <p class="tagline">Living a more natural and organic life is a philosophy not just a product certification</p>
  <div class="locations">
    <div class="location"><h3>Westbrook</h3><p>Shop 14 Westbrook Plaza, Creek Rd, Westbrook</p><p>+61 (07) 3000 1101</p><p>westbrook@mossgrovesalons.com.au</p></div>
    <div class="location"><h3>Hillcrest</h3><p>Shop 231 Hillcrest Centre, Ridge Road, Hillcrest</p><p>+61 (07) 3000 2202</p><p>hillcrest@mossgrovesalons.com.au</p></div>
    <div class="location"><h3>Riverbend</h3><p>Shop 308 Riverbend Shopping Centre, Ferry Rd Riverbend.</p><p>+61 (07) 3000 3303</p><p>riverbend@mossgrovesalons.com.au</p></div>
    <div class="location"><h3>Lakeside</h3><p>Shop 125 Lakeside Square, Prospect St, Lakeside</p><p>+61 (07) 3000 4404</p><p>lakeside@mossgrovesalons.com.au</p></div>
    <div class="location"><h3>Parkview Womens Hospital</h3><p>Wattle St, Parkview QLD 4000</p><p>+61 (07) 3000 5505</p><p>pwh@mossgrovesalons.com.au</p></div>
  </div>
</section>

<section class="card card--back">
  <div class="pill pill-left pill--dark c-ls"></div>
  <div class="pill pill-left pill--pale c-lm"></div>
  <div class="pill pill-left pill--dark c-ll"></div>
  <div class="pill pill-left pill--pale c-lx"></div>
  <div class="pill pill-right pill--dark c-rs"></div>
  <div class="pill pill-right pill--pale c-rm"></div>
  <div class="pill pill-right pill--dark c-rl"></div>
  <div class="pill pill-right pill--pale c-rx"></div>

  <!-- left menu -->
  <div class="row" style="top:44px">
    <span class="label label--left heading">CUT &amp; BLOWDRY</span>
    <span class="price size on-dark c-ls">S</span><span class="price size on-pale c-lm">M</span><span class="price size on-dark c-ll">L</span><span class="price size on-pale c-lx">XL</span>
    <span class="price size on-dark c-rs" style="left:726px">S</span><span class="price size on-pale c-rm">M</span><span class="price size on-dark c-rl">L</span><span class="price size on-pale c-rx">XL</span>
    <span class="label label--right heading">COLOUR</span>
  </div>
  <div class="row" style="top:66px"><span class="label label--left sub">LADIES</span><span class="price on-dark c-ls">$77</span><span class="price on-pale c-lm">$88</span><span class="price on-dark c-ll">$99</span><span class="price on-pale c-lx">$110</span>
    <span class="label label--right item--caps">Regrowth</span><span class="price on-dark c-rs">$83</span></div>
  <div class="row" style="top:82px"><span class="label label--left sub">FRINGE</span>
    <span class="label label--right item--caps">Full colour tint</span><span class="price on-dark c-rs">$125</span><span class="price on-pale c-rm">$145</span><span class="price on-dark c-rl">$165</span><span class="price on-pale c-rx">$185</span></div>
  <div class="row" style="top:97px"><span class="label label--left item">Trim</span><span class="price on-dark c-ls">$25</span>
    <span class="label label--right item--caps">Regrowth lightening*</span><span class="price on-dark c-rs">$165</span><span class="price on-pale c-rm">$189</span><span class="price on-dark c-rl">$209</span><span class="price on-pale c-rx">$229</span></div>
  <div class="row" style="top:111px"><span class="label label--left item">Restyle</span><span class="price on-dark c-ls">$35</span>
    <span class="label label--right item--caps">Balayage/Ombre*</span><span class="price on-pale c-rm">$275</span><span class="price on-dark c-rl">$375</span><span class="price on-pale c-rx">$475</span></div>
  <div class="row" style="top:126px"><span class="label label--left sub">MENS</span></div>
  <div class="row" style="top:142px"><span class="label label--left item">Single clipper</span><span class="price on-dark c-ls">$28</span>
    <span class="label label--right heading" style="top:-1px">VELUM</span></div>
  <div class="row" style="top:157px"><span class="label label--left item">Style cut</span><span class="price on-dark c-ls">$42</span></div>
  <div class="row" style="top:162px"><span class="label label--right item--caps">Regrowth</span><span class="price on-dark c-rs">$99</span></div>
  <div class="row" style="top:171px"><span class="label label--left sub">CHILDREN</span></div>
  <div class="row" style="top:177px"><span class="label label--right item--caps">Full colour tint</span><span class="price on-dark c-rs">$155</span><span class="price on-pale c-rm">$175</span><span class="price on-dark c-rl">$195</span><span class="price on-pale c-rx">$205</span></div>
  <div class="row" style="top:186px"><span class="label label--left item">10 and under</span><span class="price on-dark c-ls">$24</span></div>
  <div class="row" style="top:202px"><span class="label label--left item">11-16 Male</span><span class="price on-dark c-ls">$32</span></div>
  <div class="row" style="top:212px"><span class="label label--right heading">FOILS*</span></div>
  <div class="row" style="top:216px"><span class="label label--left item">11-16 Female</span><span class="price on-dark c-ls">$48</span></div>
  <div class="row" style="top:230px"><span class="label label--right item--caps">Single*</span><span class="price on-dark c-rs">$11</span><span class="price on-pale c-rm">$13</span><span class="price on-dark c-rl">$17</span><span class="price on-pale c-rx">$22</span></div>
  <div class="row" style="top:231px"><span class="label label--left item">add a wash</span><span class="price on-dark c-ls">$5</span></div>
  <div class="row" style="top:246px"><span class="label label--left sub">BLOWDRY</span><span class="price on-dark c-ls">$47</span><span class="price on-pale c-lm">$57</span><span class="price on-dark c-ll">$67</span><span class="price on-pale c-lx">$77</span></div>
  <div class="row" style="top:247px"><span class="label label--right item--caps">1/4 Head</span><span class="price on-dark c-rs">$135</span><span class="price on-pale c-rm">$155</span><span class="price on-dark c-rl">$175</span><span class="price on-pale c-rx">$195</span></div>
  <div class="row" style="top:261px"><span class="label label--left item">Shampoo &amp; dry off</span><span class="price on-dark c-ls">$25</span></div>
  <div class="row" style="top:262px"><span class="label label--right item--caps">1/2 Head</span><span class="price on-dark c-rs">$185</span><span class="price on-pale c-rm">$235</span><span class="price on-dark c-rl">$235</span><span class="price on-pale c-rx">$265</span></div>
  <div class="row" style="top:276px"><span class="label label--right item--caps">Full head</span><span class="price on-dark c-rs">$235</span><span class="price on-pale c-rm">$315</span><span class="price on-dark c-rl">$315</span><span class="price on-pale c-rx">$355</span></div>
  <div class="row" style="top:298px"><span class="label label--left heading">TREATMENTS</span></div>
  <div class="row" style="top:311px"><span class="label label--right heading">STRAIGHT</span></div>
  <div class="row" style="top:316px"><span class="label label--left item">deep treatment</span><span class="price on-dark c-ls">$35</span></div>
  <div class="row" style="top:330px"><span class="label label--left item">Head.Spa ritual</span><span class="price on-dark c-ls">$65</span>
    <span class="label label--right item--caps">Keratin straightening system</span><span class="price on-dark c-rs">$365</span><span class="price on-pale c-rm">$445</span><span class="price on-dark c-rl">$535</span><span class="price on-pale c-rx">$565</span></div>
  <div class="row" style="top:366px"><span class="label label--right note">*Includes colour match &amp; toner</span></div>
  <div class="row" style="top:368px"><span class="label label--left heading">UPSTYLE</span></div>
  <div class="row" style="top:380px"><span class="label label--right note">*Minimum 6 foils without colour</span></div>
  <div class="row" style="top:386px"><span class="label label--left item">45 minutes</span><span class="price on-dark c-ls">$105</span></div>
  <div class="row" style="top:394px"><span class="label label--right note">*Minimum charge on a Sunday is $4</span></div>
  <div class="row" style="top:401px"><span class="label label--left item">60 minutes</span><span class="price on-dark c-ls">$120</span></div>

  <div class="notice">
    <p>Pricing is indicative of average products used and time taken for each service. You will ALWAYS receive a firm price after your consultation.</p>
    <p>S to the jaw line I M to the collarbone I L to the bra strap I XL past bra strap</p>
  </div>
</section>

</body>
</html>
```